COVID-19 Accredited CME Impact Infographic

We want an infographic showing how much COVID-19 Continuing Medical Education we have accredited and its impact. Our website is at https://med.halvering.edu/cme/COVID19/education.html The attached document is intended to simply show the elements. You have complete freedom on design. We will be updating the numbers weekly so it is important that we have the files so that we can update it. This can be done in powerpoint, publisher, word, in-design, illustrator. Don't use crazy fonts that we wont have.

Target Market(s)

Internal to Halvering. We just want to show the impact of our work

Industry/Entity Type

Education

Requirements
Must have
• We must be able to update the numbers ourselves.

See attached document for the pieces that we want.

The sizes of the numbers in the attached are based on importance to us.
Nice to have
• Not mandatory but try to use these colors. https://med.halvering.edu/identity/color-palette.html

I was thinking that perhaps the big number could be done in traditional train. Like this: https://www.pictovane.com/image-illustration/flip-board-under-constuction-page-isolated-8803617452

```html
<!DOCTYPE html>
<html lang="en">
<head>
<meta charset="utf-8">
<title>COVID-19 CME Impact</title>
<link href="https://fonts.googleapis.com/css2?family=Roboto:wght@300;400;500;700;900&family=Orbitron:wght@800&display=swap" rel="stylesheet">
<style>
  :root{
    --ink:#111;
    --heading:#444;
    --muted:#888;
    --brand:#8c1515;
    --sky:#2db6fb;
    --sky-deep:#0b7fc4;
    --sky-rim:#0a5f99;
    --teal:#43c7df;
    --teal-deep:#2aa4bb;
    --lime:#c3e04a;
    --lime-deep:#97b82a;
    --gold:#e2af48;
    --gold-deep:#bd8722;
    --violet:#c962ea;
    --violet-deep:#9a3ed6;
    --mint:#45dc98;
    --mint-deep:#25b26d;
  }
  *{box-sizing:border-box;margin:0;padding:0}
  html,body{width:1200px;height:675px;overflow:hidden}
  body{
    position:relative;
    font-family:"Roboto",Arial,sans-serif;
    background:linear-gradient(160deg,#e6e6e6 0%,#f1f1f1 45%,#ffffff 100%);
    color:var(--ink);
  }
  .world-map{
    position:absolute;left:75px;top:145px;width:1060px;height:500px;
    background:radial-gradient(ellipse at 50% 45%,rgba(190,190,190,.55) 0%,rgba(205,205,205,.35) 45%,rgba(230,230,230,0) 72%);
  }
  .virus{position:absolute;border-radius:50%;
    background:radial-gradient(circle,rgba(200,70,100,.55) 0%,rgba(220,120,145,.3) 45%,rgba(240,200,210,0) 72%)}
  .virus--cme{left:735px;top:355px;width:125px;height:130px}
  .virus--corner{left:1090px;top:520px;width:130px;height:130px;opacity:.6}
  .virus--floor{left:985px;top:615px;width:140px;height:90px;opacity:.45}

  .brand-plate{
    position:absolute;left:-75px;top:-85px;width:330px;height:220px;border-radius:50%;
    background:#fff;box-shadow:6px 6px 0 #d9d6ee,10px 10px 18px rgba(120,110,170,.25);
  }
  .brand{position:absolute;left:20px;top:34px;display:flex;align-items:center;gap:10px}
  .brand__mark{width:22px;height:22px;background:var(--brand)}
  .brand__name{font-weight:500;font-size:25px;line-height:1.05;color:var(--brand)}

  .date{position:absolute;right:28px;top:24px;text-align:right}
  .date__label{font-weight:300;font-size:28px;color:var(--muted);margin-right:70px}
  .date__value{font-family:"Orbitron",monospace,sans-serif;font-weight:800;font-size:50px;letter-spacing:1px;color:#151515;line-height:1}

  .dome{
    position:absolute;left:249px;top:150px;width:250px;height:125px;
    border-radius:125px 125px 0 0;border:10px solid var(--sky-rim);border-bottom:0;
    background:linear-gradient(180deg,#2bb7fb,#1ea6ef);
    text-align:center;padding-top:52px;
    font-weight:700;font-size:30px;line-height:31px;color:var(--ink);
  }
  .headline-bar{
    position:absolute;left:147px;top:274px;width:454px;height:71px;border-radius:36px;
    background:linear-gradient(180deg,#34bdfd 0%,#1faaf2 60%,#0f92da 100%);
    box-shadow:0 4px 0 var(--sky-deep),0 6px 10px rgba(0,0,0,.15);
    display:flex;align-items:center;justify-content:center;
    font-weight:700;font-size:51px;letter-spacing:1px;color:var(--ink);
  }

  .connector{position:absolute;top:347px;border-left:1px dashed #333;width:0}
  .connector::after{content:"";position:absolute;left:-3px;bottom:-3px;width:5px;height:5px;border-radius:50%;background:#222}

  .stat{position:absolute;width:181px;text-align:center}
  .stat__label{
    position:relative;z-index:2;height:47px;border-radius:18px;
    display:flex;align-items:center;justify-content:center;
    font-weight:500;font-size:16px;color:var(--ink);
    box-shadow:0 3px 6px rgba(0,0,0,.18);
  }
  .stat__bowl{
    position:relative;z-index:1;margin:-8px auto 0;width:102px;height:54px;
    border-radius:0 0 51px 51px;border:6px solid;border-top:0;
    display:flex;align-items:flex-start;justify-content:center;padding-top:8px;
    font-weight:500;font-size:23px;color:var(--ink);
    box-shadow:0 4px 6px rgba(0,0,0,.15);
  }
  .stat--teal .stat__label{background:linear-gradient(180deg,var(--teal),var(--teal-deep))}
  .stat--teal .stat__bowl{background:var(--teal);border-color:var(--teal-deep)}
  .stat--lime .stat__label{background:linear-gradient(180deg,var(--lime),var(--lime-deep))}
  .stat--lime .stat__bowl{background:#cfe76e;border-color:var(--lime-deep)}
  .stat--gold .stat__label{background:linear-gradient(180deg,var(--gold),var(--gold-deep))}
  .stat--gold .stat__bowl{background:var(--gold);border-color:var(--gold-deep)}
  .stat--violet .stat__label{background:linear-gradient(180deg,var(--violet),var(--violet-deep))}
  .stat--violet .stat__bowl{background:var(--violet);border-color:var(--violet-deep)}
  .stat--mint .stat__label{background:linear-gradient(180deg,var(--mint),var(--mint-deep))}
  .stat--mint .stat__bowl{background:var(--mint);border-color:var(--mint-deep)}

  .title-rule{position:absolute;left:747px;top:309px;width:400px;border-top:1px solid #555}
  .title{position:absolute;left:736px;top:296px;color:var(--heading);line-height:1}
  .title__topic{display:block;font-weight:900;font-size:94px;letter-spacing:-1px}
  .title__kind{display:block;margin-left:115px;margin-top:-6px;font-weight:400;font-size:88px}
</style>
</head>
<body>
  <div class="world-map" role="img" aria-label="Faint grey world map in the background"></div>
  <div class="virus virus--cme" role="img" aria-label="Pink coronavirus illustration"></div>
  <div class="virus virus--corner" role="img" aria-label="Faded pink coronavirus illustration"></div>
  <div class="virus virus--floor" role="img" aria-label="Faded pink coronavirus illustration"></div>

  <div class="brand-plate"></div>
  <div class="brand">
    <span class="brand__mark"></span>
    <span class="brand__name">Halvering<br>Medicine</span>
  </div>

  <div class="date">
    <div class="date__label">Date:</div>
    <div class="date__value">04/ 10/20</div>
  </div>

  <div class="dome">#of total on-<br>demand views</div>
  <div class="headline-bar">1,209,987</div>

  <span class="connector" style="left:182px;height:34px"></span>
  <span class="connector" style="left:257px;height:147px"></span>
  <span class="connector" style="left:374px;height:34px"></span>
  <span class="connector" style="left:488px;height:147px"></span>
  <span class="connector" style="left:553px;height:34px"></span>

  <div class="stat stat--teal" style="left:52px;top:384px">
    <div class="stat__label">#of Activities</div>
    <div class="stat__bowl">23</div>
  </div>
  <div class="stat stat--lime" style="left:283px;top:384px">
    <div class="stat__label">#of states</div>
    <div class="stat__bowl">26</div>
  </div>
  <div class="stat stat--gold" style="left:515px;top:384px">
    <div class="stat__label">#of Countries</div>
    <div class="stat__bowl">12</div>
  </div>
  <div class="stat stat--violet" style="left:168px;top:498px">
    <div class="stat__label">#of live Learners</div>
    <div class="stat__bowl">23,098</div>
  </div>
  <div class="stat stat--mint" style="left:399px;top:498px">
    <div class="stat__label">#of CME Learners</div>
    <div class="stat__bowl">5,879</div>
  </div>

  <div class="title-rule"></div>
  <h1 class="title">
    <span class="title__topic">COVID-19</span>
    <span class="title__kind">CME</span>
  </h1>
</body>
</html>
```